KVO - Redesign (PSD Files Only)

Requirements for the site:

1. We need our logo recreated, please use the same design and change colors to work on a white background

2. The site is a "Wizard" based site, that takes the customer through the process of creating a unique web presence that suits there needs

3.Colors Needed - Main "Dark Blue" Secondary = "Dark Grey" -Other = "Light Grey and White"

4.We need a CRISP CLEAN DESIGN, simple design

5.Wireframes are a general layout and may be modified by you to enhance the design

6. We want a complete web 5.0 look with big buttons and text boxes

7.The more personality the better

8. Current Site brightmorrowco.example

9.See attachments for wireframes

10. Designer should deliver PSD files, no coding is required

11. The portfolio wireframe, should look like the design of the pixelharbor portfolio template
Updates

KEEP IT SIMPLE.,.....

We like the quillframe scaffold style of designs

```html
<!DOCTYPE html>
<html lang="en">
<head>
<meta charset="utf-8">
<title>KVO – Custom Website Design</title>
<link href="https://fonts.googleapis.com/css2?family=PT+Sans:wght@400;700&family=PT+Sans+Narrow:wght@400;700&display=swap" rel="stylesheet">
<style>
  :root {
    --blue: #1a7db4;
    --blue-soft: #dfe9ef;
    --grey-dark: #4a4a4a;
    --grey-text: #555555;
    --grey-mid: #6e6e6e;
    --hero-bg: #f0eeea;
    --footer-bg: #f2f2f2;
    --orange: #d4560f;
    --white: #ffffff;
    --social-1: #3b5a9a;
    --social-2: #3a9ad9;
    --social-3: #f26b1d;
    --social-4: #d9302b;
    --badge: #3b78d8;
  }
  * { box-sizing: border-box; margin: 0; padding: 0; }
  html, body { width: 1023px; height: 1200px; overflow: hidden; background: var(--white); }
  body { position: relative; font-family: "PT Sans", sans-serif; color: var(--grey-text); }

  /* header */
  .site-header { position: absolute; left: 0; top: 0; width: 1023px; height: 84px; background: var(--white); }
  .main-nav { position: absolute; left: 72px; top: 34px; display: flex; }
  .main-nav a { font-family: "PT Sans Narrow", sans-serif; font-size: 16px; color: var(--grey-dark); text-decoration: none; padding: 0 23px; border-left: 1px dotted #c8c8c8; line-height: 20px; }
  .main-nav a:first-child { padding-left: 0; border-left: none; }
  .social { position: absolute; left: 582px; top: 28px; display: flex; gap: 10px; }
  .social span { width: 31px; height: 31px; display: block; }
  .phone { position: absolute; left: 834px; top: 34px; font-size: 15px; color: var(--grey-dark); display: flex; align-items: center; gap: 8px; }

  /* hero */
  .hero { position: absolute; left: 0; top: 84px; width: 1023px; height: 433px; background: var(--hero-bg); }
  .hero-title { position: absolute; left: 0; width: 1023px; top: 26px; text-align: center; font-family: "PT Sans Narrow", sans-serif; font-weight: 700; font-size: 29px; color: var(--blue); }
  .hero-sub { position: absolute; left: 0; width: 1023px; top: 70px; text-align: center; font-size: 19px; color: var(--grey-mid); }
  .hero-text { position: absolute; left: 0; width: 1023px; top: 110px; text-align: center; font-size: 13.5px; color: var(--grey-text); }
  .highlight { position: absolute; border-radius: 50%; background: var(--blue-soft); }
  .bubble-text { position: absolute; text-align: center; font-size: 17px; line-height: 28px; color: var(--grey-dark); }
  .brand { position: absolute; left: 448px; top: 172px; width: 120px; text-align: center; }
  .brand-name { font-weight: 700; font-size: 34px; color: var(--blue); line-height: 38px; }
  .brand-sub { font-size: 10px; color: var(--grey-mid); white-space: nowrap; }
  .step-btn { position: absolute; left: 463px; top: 271px; width: 93px; height: 37px; background: var(--orange); color: var(--white); font-family: "PT Sans Narrow", sans-serif; font-size: 16px; line-height: 37px; text-align: center; box-shadow: 0 2px 3px rgba(0,0,0,.25); border-radius: 2px; }
  .obligation { position: absolute; left: 112px; top: 296px; width: 190px; text-align: center; font-size: 17px; color: var(--grey-dark); }
  .free-quote { position: absolute; left: 112px; top: 327px; width: 180px; text-align: center; font-family: "PT Sans Narrow", sans-serif; font-size: 19px; color: var(--blue); }
  .project-input { position: absolute; left: 380px; top: 360px; width: 202px; height: 41px; background: var(--white); border: 1px solid #dcdcdc; font-size: 13px; color: var(--grey-mid); line-height: 39px; padding-left: 12px; }
  .submit-btn { position: absolute; left: 592px; top: 360px; width: 89px; height: 41px; background: #555; color: var(--white); font-family: "PT Sans Narrow", sans-serif; font-size: 16px; line-height: 41px; text-align: center; }

  /* services */
  .service { position: absolute; top: 568px; width: 200px; }
  .service-head { display: flex; align-items: center; gap: 14px; }
  .service-icon { width: 35px; height: 35px; border-radius: 50%; background: var(--blue); display: flex; align-items: center; justify-content: center; }
  .service-title { font-size: 15.5px; color: var(--grey-dark); }
  .service-desc { margin-top: 12px; font-size: 13px; line-height: 22px; text-align: center; color: var(--grey-text); }
  .service-list { list-style: none; margin-top: 9px; }
  .service-list li { font-size: 12.5px; line-height: 27.6px; color: var(--grey-text); padding-left: 18px; position: relative; }
  .service-list li::before { content: "→"; position: absolute; left: 0; color: #999; font-size: 11px; }

  .divider { position: absolute; left: 70px; top: 808px; width: 883px; height: 16px; background: radial-gradient(ellipse at 50% 100%, rgba(0,0,0,.08), rgba(0,0,0,0) 70%); }

  /* portfolio */
  .portfolio-title { position: absolute; left: 74px; top: 860px; font-size: 19px; font-weight: 400; color: var(--grey-dark); }
  .portfolio-nav { position: absolute; left: 920px; top: 866px; }
  .work { position: absolute; top: 905px; width: 270px; height: 165px; background: var(--white); box-shadow: 0 0 5px rgba(0,0,0,.25); padding: 5px; }
  .work-shot { width: 100%; height: 100%; }

  /* footer */
  .site-footer { position: absolute; left: 0; top: 1111px; width: 1023px; height: 89px; background: var(--footer-bg); }
  .footer-links { position: absolute; left: 77px; top: 22px; font-size: 11.5px; color: var(--grey-dark); }
  .copyright { position: absolute; left: 77px; top: 50px; font-size: 11.5px; color: var(--grey-dark); }
  .partner-badge { position: absolute; left: 803px; top: 23px; width: 132px; height: 46px; background: var(--white); border: 1px solid #e2e2e2; }
  .partner-badge span { position: absolute; left: 0; top: 0; width: 46px; height: 44px; background: var(--badge); }
</style>
</head>
<body>

<header class="site-header">
  <nav class="main-nav">
    <a href="#">HOME</a><a href="#">ABOUT</a><a href="#">PORTFOLIO</a><a href="#">CONTACT US</a>
  </nav>
  <div class="social" aria-label="Social links">
    <span style="background:var(--social-1)"></span>
    <span style="background:var(--social-2)"></span>
    <span style="background:var(--social-3)"></span>
    <span style="background:var(--social-4)"></span>
  </div>
  <div class="phone">
    <svg width="12" height="18" viewBox="0 0 12 18"><path d="M9 1 C4 2 2 6 2 10 C2 14 5 17 9 17 L10 14 C7 14 6 12 6 10 C6 7 7 5 10 4 Z" fill="#555"/></svg>
    555-014-0237
  </div>
</header>

<section class="hero">
  <h1 class="hero-title">GET A CUSTOM WEBSITE DESIGN IN 21 DAYS OR LESS!</h1>
  <p class="hero-sub">Find out why were the #1 custom website design marketplace.</p>
  <p class="hero-text">Our network of designers will create 50+ web design samples for you to choose and our marketing experts will pave the way for your success.</p>

  <div class="highlight" role="img" aria-label="Hand-drawn circle around customer support note" style="left:96px;top:182px;width:220px;height:86px"></div>
  <div class="highlight" role="img" aria-label="Hand-drawn circle around moneyback note" style="left:637px;top:166px;width:222px;height:86px"></div>
  <div class="highlight" role="img" aria-label="Hand-drawn circle around savings note" style="left:720px;top:277px;width:221px;height:86px"></div>

  <p class="bubble-text" style="left:126px;top:211px;width:160px">24/7 Customer<br>Support</p>
  <p class="bubble-text" style="left:668px;top:194px;width:160px">100% Moneyback<br>Guarantee</p>
  <p class="bubble-text" style="left:750px;top:304px;width:160px">Save 1000’ s<br>on web design</p>

  <div class="brand">
    <div class="brand-name">KVO</div>
    <div class="brand-sub">Kestrel Vale Online</div>
  </div>
  <div class="step-btn">STEP 1</div>

  <p class="obligation">100% No Obligation</p>
  <p class="free-quote">FREE WEB QUOTE</p>
  <div class="project-input">Name your project</div>
  <div class="submit-btn">SUBMIT</div>
</section>

<section class="service" style="left:75px">
  <div class="service-head">
    <span class="service-icon"><svg width="18" height="18" viewBox="0 0 18 18" fill="none" stroke="#fff" stroke-width="1.5"><path d="M9 3 L16 7 L9 11 L2 7 Z"/><path d="M2 10 L9 14 L16 10"/></svg></span>
    <span class="service-title">Why choose KVO?</span>
  </div>
  <p class="service-desc">Claritas est etiam proceissus dyna micus, qui sequitur mutation.</p>
  <ul class="service-list"><li>Dedicated Project Manager</li><li>Single point od contact</li><li>Marketing Coaches</li><li>Low Cost</li></ul>
</section>

<section class="service" style="left:312px">
  <div class="service-head">
    <span class="service-icon"><svg width="18" height="18" viewBox="0 0 18 18" fill="none" stroke="#fff" stroke-width="1.5"><path d="M9 2 L16 5.5 L16 12.5 L9 16 L2 12.5 L2 5.5 Z"/><path d="M2 5.5 L9 9 L16 5.5 M9 9 L9 16"/></svg></span>
    <span class="service-title">Web Services</span>
  </div>
  <p class="service-desc">Claritas est etiam proceissus dyna micus, qui sequitur mutation.</p>
  <ul class="service-list"><li>Dedicated Project Manager</li><li>Single point od contact</li><li>Marketing Coaches</li><li>Low Cost</li></ul>
</section>

<section class="service" style="left:542px">
  <div class="service-head">
    <span class="service-icon"><svg width="18" height="18" viewBox="0 0 18 18" fill="none" stroke="#fff" stroke-width="1.8"><circle cx="7" cy="10" r="3"/><circle cx="13.5" cy="5" r="2"/><path d="M7 4.5 V6 M7 14 V15.5 M1.5 10 H3 M11 10 H12.5"/></svg></span>
    <span class="service-title">Marketing Services</span>
  </div>
  <p class="service-desc">Claritas est etiam proceissus dyna micus, qui sequitur mutation.</p>
  <ul class="service-list"><li>Dedicated Project Manager</li><li>Single point od contact</li><li>Marketing Coaches</li><li>Low Cost</li></ul>
</section>

<section class="service" style="left:765px">
  <div class="service-head">
    <span class="service-icon"><svg width="18" height="18" viewBox="0 0 18 18" fill="none" stroke="#fff" stroke-width="1.5"><path d="M2 8 L16 2 L11 16 L8 10 Z M8 10 L16 2"/></svg></span>
    <span class="service-title">Maintaince Services</span>
  </div>
  <p class="service-desc">Claritas est etiam proceissus dyna micus, qui sequitur mutation.</p>
  <ul class="service-list"><li>Dedicated Project Manager</li><li>Single point od contact</li><li>Marketing Coaches</li><li>Low Cost</li></ul>
</section>

<div class="divider"></div>

<h2 class="portfolio-title">Portfolio</h2>
<svg class="portfolio-nav" width="26" height="16" viewBox="0 0 26 16" fill="none" stroke="#777" stroke-width="2"><path d="M9 1 L2 8 L9 15 M17 1 L24 8 L17 15"/></svg>

<div class="work" style="left:74px">
  <div class="work-shot" role="img" aria-label="Restaurant website screenshot with a pasta dish" style="background:linear-gradient(160deg,#5b5a16 0%,#2a2410 45%,#7a3a12 75%,#1a1208 100%)"></div>
</div>
<div class="work" style="left:373px">
  <div class="work-shot" role="img" aria-label="Island gift shop website screenshot with palm leaves and jars" style="background:linear-gradient(180deg,#f4f4f4 0%,#f4f4f4 20%,#1f4a3e 22%,#2f6a66 55%,#c9bfa6 75%,#3a3a3a 100%)"></div>
</div>
<div class="work" style="left:677px">
  <div class="work-shot" role="img" aria-label="Fitness gym franchise website screenshot with a gym interior" style="background:linear-gradient(150deg,#111 0%,#1a1a1a 25%,#6b4a2a 50%,#2a1c12 80%,#0c0c0c 100%)"></div>
</div>

<footer class="site-footer">
  <p class="footer-links">Terms and Condition &nbsp;|&nbsp; Privacy Policy</p>
  <p class="copyright">Copyrights 2014. All Rights Reserved.</p>
  <div class="partner-badge" aria-label="Partner badge"><span></span></div>
</footer>

</body>
</html>
```